Not another boring Business Card Design Project

This is not another boring Business Card Design Project.

We are looking for the weirdest, wackiest most boundary pushing designs that you can come up with.

If you believe that design can be fun, energetic, crazy, unpredictable, beautiful and eye-catching then read on… this project is for you.

We are Tolvin Presk and we print plastic cards.

We are running a Plastic Card Design Competition.

And we need a plastic card to advertise the competition to graphic designers just like you.

The design needs to make your average designers’ jaws drop and their eyes pop out.

You can do what you wish with the card design, so long as it stands out.

We like these designs, designs that stretch the boundaries and become something beyond just another business card:

http://quorvamedia.net/wp-content/uploads/2009/03/b48.jpg
Designer - http://www.pelvanworks.com/

http://quorvamedia.net/wp-content/uploads/2009/03/b41.jpg
Designer - http://renolbrakstad.com/

http://images.plinthhive.com/designs/44195_732292_37774_thumbnail.jpg
Designer- Zentro Media at Plinth Hive

http://images.plinthhive.com/designs/44195_717529_37774_thumbnail.jpg
Designer - Zentro Media at Plinth Hive

http://quorvamedia.net/wp-content/uploads/2009/03/b11.jpg
Designer - http://www.wk7studio.com/

http://quorvamedia.net/wp-content/uploads/2009/03/b16.jpg
Designer - http://www.pebbletumbler.com/

Reason: A number of designers have said they want to submit designs and haven't yet done so, we want to give them time.

Reason: We've extended the deadline by 4 days for those who want to submit their designs over the weekend and give ourselves time to judge them

Plastic

• The design needs to contain this link: lnk.example/QzRpLk and any other detail that will encourage competition entry. The design will be printed on plastic.
• No borders (when plastic cards are punched to shape and size there is movement of 1 - 2mm, borders highlight this movement).

Keep text 3mm away from edges of the cards.

Please don't create designs to be produced on clear/transparent plastic.

```html
<!DOCTYPE html>
<html lang="en">
<head>
<meta charset="utf-8">
<title>Nadia Voss — Graphic Designer Plastic Card</title>
<link rel="stylesheet" href="https://fonts.googleapis.com/css2?family=Arimo:wght@400;700&family=Open+Sans:wght@400;700&family=Mrs+Saint+Delafield&display=swap">
<style>
  :root {
    --canvas-bg: #f4f4f2;
    --card-dark: #3a3a3c;
    --card-light: #dcdad6;
    --ink: #1a1a1a;
    --ink-script: #5e5e60;
    --name-grey: #b4b4b6;
    --white: #ffffff;
    --seed-teal: #1aa3b8;
    --seed-green: #8cc63f;
    --seed-yellow: #e0c21a;
    --seed-orange: #f08a1c;
    --seed-red: #e2223a;
    --seed-purple: #8a2a9c;
    --seed-violet: #3a2a8c;
  }
  * { box-sizing: border-box; margin: 0; padding: 0; }
  html, body { width: 1200px; height: 1200px; overflow: hidden; }
  body { background: var(--canvas-bg); position: relative; }

  .card {
    position: absolute;
    left: 220px;
    width: 760px;
    height: 477px;
    border-radius: 34px;
    overflow: hidden;
  }
  .card--front { top: 90px; background: var(--card-dark); }
  .card--back { top: 630px; background: var(--card-light); }

  /* Front: scattered seeds and faint dandelion */
  .seed-field {
    position: absolute;
    left: 36px; top: 30px;
    width: 690px; height: 150px;
    border-radius: 24px;
    background: linear-gradient(90deg,
      var(--seed-teal), var(--seed-green) 25%, var(--seed-yellow) 40%,
      var(--seed-orange) 55%, var(--seed-red) 68%, var(--seed-purple) 85%, var(--seed-violet));
    opacity: 0.28;
  }
  .dandelion-faint {
    position: absolute;
    left: 210px; top: 250px;
    width: 440px; height: 260px;
    background: radial-gradient(ellipse at 50% 70%, rgba(150,150,152,0.45), rgba(150,150,152,0) 70%);
  }
  .contact {
    position: absolute;
    left: 160px; top: 230px;
    font-family: "Arimo", Arial, sans-serif;
    font-size: 27px;
    line-height: 1.3;
  }
  .contact__name { color: var(--name-grey); font-weight: 700; }
  .contact__role { color: var(--white); }
  .contact__phone { color: var(--white); }
  .contact__email { color: var(--name-grey); margin-left: 8px; }

  /* Back: services list with quote */
  .dandelion-bright {
    position: absolute;
    left: 120px; top: 180px;
    width: 620px; height: 340px;
    background: radial-gradient(ellipse at 52% 78%, rgba(255,255,255,0.95), rgba(255,255,255,0.35) 30%, rgba(255,255,255,0) 68%);
  }
  .services {
    position: absolute;
    left: 40px; right: 40px; top: 34px;
    font-family: "Open Sans", Arial, sans-serif;
    color: var(--ink);
  }
  .services__row {
    display: flex;
    justify-content: space-between;
    font-size: 33px;
    letter-spacing: 0.2px;
    line-height: 1;
    text-transform: uppercase;
  }
  .services__row b { font-weight: 700; }
  .services__row span { font-weight: 400; }
  .quote {
    font-family: "Mrs Saint Delafield", cursive;
    color: var(--ink-script);
    font-size: 50px;
    line-height: 1;
    margin: -6px 0 6px 0;
    white-space: nowrap;
    letter-spacing: 1px;
  }
  .specs {
    position: absolute;
    left: 50px; bottom: 34px;
    font-family: "Open Sans", Arial, sans-serif;
    font-size: 18px;
    color: var(--ink);
  }
</style>
</head>
<body>
  <section class="card card--front" aria-label="Card front">
    <div class="seed-field" role="img" aria-label="Colourful dandelion seeds drifting across the top of the card"></div>
    <div class="dandelion-faint" role="img" aria-label="Faint grey dandelion head rising from the bottom edge"></div>
    <div class="contact">
      <p><span class="contact__name">nadia voss</span> <span class="contact__role">graphic designer</span></p>
      <p><span class="contact__phone">+230 555 0142</span><span class="contact__email">nadiavs@inkmail.com</span></p>
    </div>
  </section>

  <section class="card card--back" aria-label="Card back">
    <div class="dandelion-bright" role="img" aria-label="White dandelion head bursting behind the text"></div>
    <div class="services">
      <p class="services__row"><b>Advertising</b><span>Logo Design</span><b>Corporate</b></p>
      <p class="quote">creativity involves breaking out</p>
      <p class="services__row"><b>Identity</b><span>Brand</span><span>Identity</span><b>Packaging</b></p>
      <p class="quote">of established patterns in order to</p>
      <p class="services__row"><span>Print Media</span><b>Annual Reports</b><span>Posters</span></p>
      <p class="quote">look at things in a different way.</p>
      <p class="services__row"><b>Magazines</b><span>Brochures</span><b>Website Design</b></p>
    </div>
    <p class="specs">86mmx54mm / 760micron /100% plastic / cmyk / lnk.example/QzRpLk</p>
  </section>
</body>
</html>
```